Business cards for law firm with global theme

I'd like business cards with contact info for two offices. They should include the colors and font of the new logo design, which is a stylized globe with an "F" in it. The feel should be very modern and professional.

```html
<!DOCTYPE html>
<html lang="en">
<head>
<meta charset="UTF-8">
<title>Verantis Law – Business Cards</title>
<link href="https://fonts.googleapis.com/css2?family=Questrial&display=swap" rel="stylesheet">
<style>
  :root {
    --navy: #0b3a6e;
    --sky: #1aa3e0;
    --paper: #ffffff;
    --backdrop: #e9ecef;
    --back-light: #0aa6e4;
    --back-dark: #003a74;
  }
  * { margin: 0; padding: 0; box-sizing: border-box; }
  html, body { width: 1200px; height: 1108px; overflow: hidden; }
  body {
    background: var(--backdrop);
    font-family: "Questrial", sans-serif;
    display: flex;
    align-items: center;
    justify-content: center;
    gap: 64px;
  }
  .card {
    width: 420px;
    height: 735px;
    border-radius: 22px;
    position: relative;
    overflow: hidden;
    box-shadow: 0 10px 30px rgba(0,0,0,0.18);
  }
  .card-front {
    background: var(--paper);
    display: flex;
    flex-direction: column;
    align-items: center;
    padding-top: 96px;
    color: var(--navy);
  }
  .brand {
    display: flex;
    align-items: center;
    gap: 18px;
  }
  .brand-dot {
    width: 66px; height: 66px;
    border-radius: 50%;
    background: var(--sky);
  }
  .brand-name {
    font-size: 36px;
    color: var(--navy);
    line-height: 1.05;
    letter-spacing: 0.5px;
  }
  .brand-rule {
    width: 300px;
    height: 1.5px;
    background: var(--sky);
    margin: 18px 0 58px;
  }
  .person-name { font-size: 25px; letter-spacing: 1px; }
  .person-title { font-size: 20px; color: var(--sky); margin-top: 2px; }
  .divider {
    width: 150px; height: 1px;
    background: var(--sky);
    opacity: 0.5;
    margin: 16px 0 14px;
  }
  .office {
    text-align: center;
    font-size: 20px;
    line-height: 1.28;
    margin-bottom: 14px;
  }
  .office-label { color: var(--sky); font-size: 22px; letter-spacing: 1px; }
  .web { font-size: 21px; letter-spacing: 2px; }
  .web .accent { color: var(--sky); }

  .card-back {
    background: linear-gradient(215deg, var(--back-light) 0%, #0474b4 45%, var(--back-dark) 100%);
  }
  .back-pattern {
    position: absolute; inset: 0;
    background: linear-gradient(215deg, rgba(255,255,255,0.04), rgba(0,0,0,0.06));
  }
  .back-mark {
    position: absolute;
    left: 50%; top: 58%;
    transform: translate(-50%, -50%);
    display: flex; align-items: center; gap: 10px;
  }
  .back-mark .brand-dot { width: 40px; height: 40px; background: var(--paper); }
  .back-mark .brand-name { color: var(--paper); font-size: 20px; }
</style>
</head>
<body>
  <section class="card card-front">
    <div class="brand">
      <div class="brand-dot"></div>
      <div class="brand-name">VERANTIS<br>LAW</div>
    </div>
    <div class="brand-rule"></div>

    <div class="person-name">DANIEL REEVES</div>
    <div class="person-title">Managing Director</div>
    <div class="divider"></div>

    <div class="office">
      <div class="office-label">VERANTIS OFFICE</div>
      <div>P: 055-210 384 617</div>
      <div>E: hello@verantislaw.com</div>
      <div>Address line goes here</div>
      <div>45452,Country Name</div>
    </div>
    <div class="office">
      <div class="office-label">VERANTIS OFFICE</div>
      <div>P: 055-210 384 617</div>
      <div>E: hello@verantislaw.com</div>
      <div>Address line goes here</div>
      <div>45452,Country Name</div>
    </div>

    <div class="divider"></div>
    <div class="web">www.<span class="accent">verantislaw</span>.com</div>
  </section>

  <section class="card card-back">
    <div class="back-pattern" role="img" aria-label="Embossed repeating brand-mark pattern across the blue card back"></div>
    <div class="back-mark">
      <div class="brand-dot"></div>
      <div class="brand-name">VERANTIS</div>
    </div>
  </section>
</body>
</html>
```